Flyer Design Project

We are offering a new class on cyber crime and want to advertise this course to students. We would like to see a design that is eye catching and coveys the goals of the course, when it meets and a brief abstract for the class.

The course will focus on the economics of cyber crime so including one or two graphics that get across this point would be good.

Requirements
Must have
• Course name "Cyber Crime"
Call number "CS 795 - 004"
Course meeting time (day of week and time) Tue. 4:30-7:10pm
Course goals
Course abstract

```html
<!DOCTYPE html>
<html lang="en">
<head>
<meta charset="utf-8">
<title>Cyber Crime – CS 795 / ISA 797</title>
<link rel="stylesheet" href="https://fonts.googleapis.com/css2?family=Anton&family=Arimo:ital,wght@0,400;0,700;1,700&display=swap">
<style>
  :root {
    --wall-top: #ffffff;
    --wall-mid: #dde6ec;
    --wall-low: #b9cad6;
    --floor: #c9d7e1;
    --teal: #2b6c87;
    --teal-dark: #1f5e7a;
    --red: #e31e24;
    --ink: #1b1b1b;
    --white: #ffffff;
    --doorway-top: #3a3f3a;
    --doorway-low: #1a1d20;
  }
  * { margin: 0; padding: 0; box-sizing: border-box; }
  html, body { width: 927px; height: 1200px; overflow: hidden; }
  body { font-family: "Arimo", Arial, sans-serif; color: var(--ink); }

  .flyer {
    position: relative;
    width: 927px;
    height: 1200px;
    overflow: hidden;
    background:
      radial-gradient(ellipse 70% 40% at 45% 18%, var(--wall-top) 0%, rgba(255,255,255,0) 70%),
      linear-gradient(180deg, #f4f7f9 0%, var(--wall-mid) 32%, var(--floor) 41%, #d4e0e8 52%, var(--wall-low) 100%);
  }

  .doorway-scene {
    position: absolute;
    left: 605px;
    top: 43px;
    width: 242px;
    height: 442px;
    background: linear-gradient(180deg, var(--doorway-top) 0%, var(--doorway-low) 100%);
  }

  .title-cyber {
    position: absolute;
    left: 182px;
    top: 70px;
    font-family: "Arimo", Arial, sans-serif;
    font-weight: 700;
    font-size: 64px;
    letter-spacing: 1px;
    color: var(--red);
    line-height: 1;
  }
  .title-crime {
    position: absolute;
    left: 60px;
    top: 132px;
    width: 505px;
    height: 262px;
  }
  .title-crime text {
    font-family: "Anton", Impact, sans-serif;
    fill: var(--teal);
  }

  .course-code {
    position: absolute;
    left: 142px;
    top: 438px;
    font-size: 40px;
    color: #111;
    line-height: 1;
  }
  .schedule {
    position: absolute;
    left: 60px;
    top: 502px;
    width: 520px;
    text-align: center;
    font-weight: 700;
    font-style: italic;
    font-size: 40px;
    line-height: 54px;
    color: var(--red);
  }

  .section-label {
    position: absolute;
    left: 98px;
    width: 272px;
    height: 37px;
    background: var(--teal-dark);
    color: var(--white);
    font-weight: 700;
    font-style: italic;
    font-size: 18px;
    line-height: 37px;
    padding-left: 22px;
  }
  .section-label.goals { top: 670px; }
  .section-label.abstract { top: 843px; }

  .goal-list {
    position: absolute;
    left: 119px;
    top: 734px;
    width: 690px;
    list-style: none;
    font-size: 17.5px;
    line-height: 24px;
  }
  .goal-list li { display: flex; margin-bottom: 20px; }
  .goal-list .num { width: 34px; flex: none; }

  .abstract-text {
    position: absolute;
    left: 116px;
    top: 892px;
    width: 690px;
    font-size: 17.5px;
    line-height: 27.4px;
    text-align: justify;
    hyphens: auto;
  }

  .more-info {
    position: absolute;
    left: 0;
    top: 1094px;
    width: 927px;
    text-align: center;
    font-size: 17.5px;
  }
  .link-bar {
    position: absolute;
    left: 43px;
    top: 1130px;
    width: 841px;
    height: 43px;
    background: var(--red);
    color: var(--white);
    text-align: center;
    font-weight: 700;
    font-size: 26px;
    line-height: 43px;
  }
</style>
</head>
<body>
<main class="flyer">
  <div class="doorway-scene" role="img" aria-label="Dark open doorway in a bright wall, sealed off with crime-scene tape"></div>

  <h1>
    <span class="title-cyber">CYBER</span>
    <svg class="title-crime" viewBox="0 0 505 262" aria-label="Crime">
      <text x="0" y="258" font-size="318" textLength="500" lengthAdjust="spacingAndGlyphs">Crime</text>
    </svg>
  </h1>

  <p class="course-code">CS 795 / ISA 797</p>
  <p class="schedule">Fall 2012<br>Tuesday, 4:30-7:10 pm</p>

  <h2 class="section-label goals">THE GOAL OF THE CLASS :</h2>
  <ol class="goal-list">
    <li><span class="num">1)</span><span>Understand how modern cyber-crime operates on a technical and economic level</span></li>
    <li><span class="num">2)</span><span>Analyze some of the potential places to intervene at an economic, technical and policy level.</span></li>
  </ol>

  <h2 class="section-label abstract">COURSE ABSTRACT :</h2>
  <p class="abstract-text">Arguably the single most significant change in the cyber-security landscape has been the explosive rise of profit-fueled cyber-crime. Obtaining a detailed, structural understanding of how profit-driven cyber crime works — its underlying economics and associated business practices — has the potential to illuminate new defensive measures that might prove far more efficient for countering attacks than purely technical measures. This research seminar will delve into our current understanding of the economics of cyber-crime.</p>

  <p class="more-info">For more details please go to :</p>
  <p class="link-bar">http://cs.northfield.edu/~harlow/crime.html</p>
</main>
</body>
</html>
```